Banner for Vet Hospital 5m x 1.2m - Heat Stroke

Meadowlark Pet Hospital needs a Heat Stroke Banner for Summer.
The banner will be 5000mm long and 1200mm tall.

Our region has been hot this year and this summer is going to be extremely hot.
I want to warn people about heat stroke.
I want you to create a heat stroke banner that conveys the symptoms of heat stroke.

Pictures are better than words.
There should be IMAGES and WORDS that can be seen from the road 30m away and maybe some smaller words for people to read as they walk past.

Here are some of the signs of Heat Stroke:
- Panting which increases as heatstroke progresses
- Drooling, salivating
- Agitation, restlessness
- Very red or pale gums
- Bright red tongue
- Increased heart rate
- Breathing distress
- Vomiting Diarrhea (possibly with blood)
- Signs of mental confusion, delirium
- Dizziness, staggering
- Lethargy, weakness
- Muscle tremors
- Seizures
- Collapsing and lying down
- Little to no urine production
- Coma

I have attached characters that we often use in our advertising. They are optional.
I have done a mock up of the design I imagine. You could refine this design or make your own....or both.

Target Market(s)

Women aged 20 to 50.

Industry/Entity Type

Veterinary

Font styles to use
Sans Serif

Colors
fbed22
f78f20
ec1f27
ffffff

Requirements
Must have
• Heat Stroke Symtpms.
• Heat Stroke Warning.
• Summer theme.
Nice to have
• Bright colours.

```html
<!DOCTYPE html>
<html lang="en">
<head>
<meta charset="utf-8">
<title>Meadowlark Pet Hospital – Summer Heat Stroke Banner</title>
<link rel="stylesheet" href="https://fonts.googleapis.com/css2?family=Roboto+Condensed:wght@400;700;800&display=swap">
<style>
  :root {
    --sun-yellow: #fbed22;
    --sun-gold: #fcc21b;
    --heat-orange: #f78f20;
    --alert-red: #ec1f27;
    --white: #ffffff;
    --leaf-green: #8cc63f;
    --brown: #4a2e1a;
    --page-bg: #eeeeee;
  }
  * { margin: 0; padding: 0; box-sizing: border-box; }
  html, body {
    width: 1200px; height: 926px; overflow: hidden;
    background: var(--page-bg);
    font-family: "Roboto Condensed", Arial, sans-serif;
  }
  .banner {
    position: absolute; left: 20px; top: 324px;
    width: 1160px; height: 278px; overflow: hidden;
    background:
      radial-gradient(ellipse 380px 260px at 33% 55%, var(--sun-yellow) 0%, var(--sun-gold) 40%, rgba(247,143,32,0) 80%),
      linear-gradient(90deg, var(--sun-gold) 0%, var(--heat-orange) 55%, var(--heat-orange) 100%);
    color: var(--brown);
  }
  .brand {
    position: absolute; left: 16px; top: 78px; width: 156px;
  }
  .brand-dot {
    width: 34px; height: 34px; border-radius: 50%;
    background: var(--leaf-green); margin-bottom: 12px;
  }
  .brand-name {
    font-size: 20px; font-weight: 700; line-height: 1.15;
    color: var(--brown); text-transform: uppercase; white-space: nowrap;
  }
  .headline-kicker {
    position: absolute; left: 260px; top: 14px;
    font-size: 46px; font-weight: 700; letter-spacing: -0.5px; white-space: nowrap;
  }
  .headline-main {
    position: absolute; left: 186px; top: 52px;
    font-size: 96px; font-weight: 800; letter-spacing: -2px; line-height: 1; white-space: nowrap;
    -webkit-text-stroke: 2px var(--alert-red);
    paint-order: stroke fill;
  }
  .symptoms {
    position: absolute; left: 200px; top: 162px;
    display: flex; gap: 18px;
  }
  .symptom { width: 96px; text-align: center; }
  .symptom-art {
    width: 86px; height: 86px; margin: 0 auto;
    border-radius: 14px; border: 3px solid var(--alert-red);
  }
  .symptom-panting .symptom-art { background: radial-gradient(circle, #c98a55, #7a4a2a); }
  .symptom-gums .symptom-art { background: radial-gradient(circle, #e0636a, #8d1f27); }
  .symptom-collapse .symptom-art { background: radial-gradient(circle, #b08968, #6b4a33); }
  .symptom-label {
    margin-top: 4px; font-size: 16px; font-weight: 700; line-height: 1.1;
    white-space: nowrap;
  }
  .warning-band {
    position: absolute; left: 700px; top: 100px; right: 0; height: 64px;
    background: var(--leaf-green);
    border-radius: 8px 0 0 8px;
    display: flex; align-items: center; padding-left: 26px;
    font-size: 46px; font-weight: 700; color: var(--white); white-space: nowrap;
  }
  .phone {
    position: absolute; left: 600px; top: 170px;
    font-size: 64px; font-weight: 800; letter-spacing: -0.5px; line-height: 1; white-space: nowrap;
  }
  .website {
    position: absolute; left: 600px; top: 236px;
    font-size: 31px; font-weight: 700; line-height: 1; white-space: nowrap;
  }
</style>
</head>
<body>
  <main class="banner">
    <div class="brand">
      <div class="brand-dot"></div>
      <div class="brand-name">Meadowlark Pet<br>Hospital</div>
    </div>

    <div class="headline-kicker">Get Ready for</div>
    <h1 class="headline-main">Summer Heat</h1>

    <div class="symptoms">
      <div class="symptom symptom-panting">
        <div class="symptom-art" role="img" aria-label="Illustration of a dog panting heavily from heat stroke"></div>
        <div class="symptom-label">Heavy panting</div>
      </div>
      <div class="symptom symptom-gums">
        <div class="symptom-art" role="img" aria-label="Illustration of very red gums and a bright red tongue"></div>
        <div class="symptom-label">Red gums</div>
      </div>
      <div class="symptom symptom-collapse">
        <div class="symptom-art" role="img" aria-label="Illustration of a pet staggering and collapsing"></div>
        <div class="symptom-label">Collapsing</div>
      </div>
    </div>

    <div class="warning-band">Heat Stroke Warning</div>
    <div class="phone">02 5550 1938</div>
    <div class="website">meadowlarkpethospital.com.au</div>
  </main>
</body>
</html>
```